Landing Page Design for Cancer Article

We need to have relevant custom graphics and images incorporated with the text of the Google Doc. The Google Doc contains content for an article that informs users about Stomach Cancer. The article was written by a non-profit organization that promotes education and awareness about this disease. Their website address is www.velundaro.org so you can see their current color theme and branding.

Basically, we're just looking to make the article look more polished. We don't want users coming to the article and just see a wall of text. We'd like graphics and images relevant to the content. Also the layout to make readability easier. Let me know if you have more questions.

https://files.plimsvex.com/document/d/7KqWbRtXmNpLsYdH3cVfJzUeAgOiB/edit?usp=sharing&ouid=402918736455102938476&rtpof=true&sd=true

```html
<!DOCTYPE html>
<html lang="en">
<head>
<meta charset="utf-8">
<title>About Stomach Cancer – Velundaro Family Foundation</title>
<link href="https://fonts.googleapis.com/css2?family=Nunito+Sans:wght@400;600;700;800&display=swap" rel="stylesheet">
<style>
:root{
  --ink:#1d1f2b;
  --text:#3a3d4a;
  --blue:#0a5fb8;
  --blue-deep:#0b5ab0;
  --blue-soft:#e8f3fb;
  --grey-bg:#f1f1f3;
  --dark:#1c1c26;
  --dark-2:#15151e;
  --orange:#f6a21e;
  --white:#ffffff;
}
*{box-sizing:border-box;margin:0;padding:0}
html,body{width:1200px;height:3766px;overflow:hidden}
body{font-family:"Nunito Sans",Arial,sans-serif;color:var(--text);background:var(--white);font-size:11px;line-height:1.45}
section,header,footer{position:relative;width:1200px}
.abs{position:absolute}
h1,h2,h3{color:var(--ink);font-weight:700}
.rule{width:42px;height:2px;background:var(--blue);margin-top:14px}
.rule.center{margin:14px auto 0}
.img{position:absolute;border-radius:2px}
ul{list-style:none}
.tri li{position:relative;padding-left:14px;margin-bottom:9px}
.tri li::before{content:"";position:absolute;left:2px;top:4px;border-left:4px solid var(--ink);border-top:3px solid transparent;border-bottom:3px solid transparent}

/* top strip */
.topbar{height:25px;background:var(--dark)}
.topbar .date{position:absolute;left:8px;top:3px;color:#fff;font-size:7px;line-height:1;font-weight:700}
.topbar .date b{color:var(--blue);font-size:16px;float:left;margin-right:3px}

/* header */
.site-header{height:64px;background:#fff;border-bottom:1px solid #eee}
.brand{position:absolute;left:20px;top:20px;display:flex;align-items:center;gap:6px;font-weight:800;color:var(--blue);font-size:11px}
.brand i{display:block;width:16px;height:16px;border:2px solid var(--blue);border-radius:50%}
.nav{position:absolute;left:300px;top:24px;display:flex;gap:30px;font-size:10.5px;font-weight:600;color:var(--ink)}
.nav .active{color:var(--blue)}
.nav .dd::after{content:"⌄";margin-left:6px;color:#888}
.donate-top{position:absolute;left:1114px;top:14px;width:77px;height:33px;border-radius:17px;background:var(--orange);border:2px solid #e07b0a;color:#1d1f2b;font-size:8.5px;font-weight:700;display:flex;align-items:center;justify-content:center;gap:3px}

/* hero */
.hero{height:314px;background:var(--grey-bg)}
.hero h1{position:absolute;left:234px;top:36px;width:260px;font-size:16px;line-height:1.4}
.hero .rule{position:absolute;left:234px;top:118px;margin:0}
.hero p{position:absolute;left:234px;top:140px;width:260px}
.hero .img{left:536px;top:28px;width:427px;height:254px;background:linear-gradient(135deg,#0b3f6f,#3c8ac0 45%,#a7d3ef 60%,#1d5c8f)}

/* causes */
.causes{height:562px}
.sec-title{text-align:center;font-size:15px;padding-top:40px}
.sec-lead{text-align:center;width:520px;margin:12px auto 0}
.causes .img{left:234px;top:154px;width:326px;height:356px;background:radial-gradient(circle at 58% 62%,#ff7a2e 0,#c8331a 18%,#0e3f7a 45%,#04152f 80%)}
.cond-box{position:absolute;left:593px;top:152px;width:372px;height:234px;background:var(--blue-soft);padding:22px 16px}
.cond-box h3{font-size:11.5px;font-weight:600;position:relative;padding-left:14px}
.cond-box h3::before{content:"";position:absolute;left:2px;top:5px;border-left:4px solid var(--ink);border-top:3px solid transparent;border-bottom:3px solid transparent}
.dots{margin:14px 0 0 14px;font-size:10px}
.dots li{position:relative;padding-left:16px;margin-bottom:5px}
.dots li::before{content:"";position:absolute;left:0;top:4px;width:5px;height:5px;border-radius:50%;background:var(--blue)}
.dots li.gap{margin-top:14px;margin-bottom:14px}
.risk-list{position:absolute;left:593px;top:402px;width:380px;font-size:10px}
.risk-list li{margin-bottom:10px}

/* symptoms */
.symptoms{height:516px;background:var(--grey-bg)}
.symptoms .sec-title{padding-top:28px}
.card{position:absolute;top:93px;width:356px;height:393px;background:#fff;box-shadow:0 2px 6px rgba(0,0,0,.08)}
.card .img{position:relative;display:block;width:100%;height:181px;border-radius:0}
.card.early{left:234px}
.card.early .img{background:linear-gradient(135deg,#3b3b3f,#7d6a5e 45%,#c48a6b 60%,#5a5a60)}
.card.late{left:609px}
.card.late .img{background:linear-gradient(135deg,#5e4a34,#9a6a46 45%,#7e7a58 70%,#3d3a2c)}
.card-body{padding:18px 25px}
.card-body h3{font-size:11px;font-weight:700;line-height:1.5;margin-bottom:12px}
.card .tri{font-size:9.5px}
.card .tri li{margin-bottom:6px;padding:2px 0 2px 16px}
.card .tri li.hl{background:var(--blue-soft);width:max-content;padding-right:10px}
.card.late .tri li.hl{width:214px}

/* diagnosis */
.diagnosis{height:631px}
.diagnosis h2{position:absolute;left:234px;top:68px;font-size:15px}
.diagnosis .rule{position:absolute;left:234px;top:94px;margin:0}
.diagnosis .intro{position:absolute;left:234px;top:112px;width:235px}
.diagnosis .img.a{left:574px;top:33px;width:389px;height:234px;background:linear-gradient(135deg,#6c6c6c,#e9ecef 40%,#8fc6ee 55%,#777 100%)}
.diagnosis .img.b{left:234px;top:301px;width:339px;height:291px;background:radial-gradient(circle at 52% 55%,#c98a2a 0,#8b5a2a 16%,#1c4f9c 40%,#0b2c6c 80%)}
.imaging{position:absolute;left:604px;top:300px;width:350px}
.imaging h3{font-size:11px;font-weight:700}
.imaging .tri{margin:22px 0 0 12px;font-size:9.5px;line-height:1.45}
.imaging .tri li{margin-bottom:18px;padding-left:16px}
.imaging .after{margin-left:12px;font-size:9.5px}

/* treatments */
.treatments{height:541px;background:var(--blue-deep);color:#fff}
.treatments h2{position:absolute;left:234px;top:40px;font-size:15px;color:#fff}
.treatments .rule{position:absolute;left:234px;top:66px;margin:0;background:#fff}
.treat-text{position:absolute;left:234px;top:87px;width:377px;font-size:9.6px;line-height:1.27;text-align:justify;color:#eef4fb}
.treat-text p{margin-bottom:11px}
.treatments .img{left:652px;top:91px;width:313px;height:399px;background:linear-gradient(160deg,#cfd6dd,#f4f2f0 40%,#e6bcc3 75%,#3f7fc2)}

/* survival */
.survival{height:462px}
.survival .img{left:236px;top:51px;width:309px;height:368px;background:radial-gradient(circle at 60% 45%,#f3ede5 0,#c9b097 35%,#b59878 70%)}
.survival h2{position:absolute;left:589px;top:60px;font-size:15px}
.survival .rule{position:absolute;left:589px;top:86px;margin:0}
.surv-text{position:absolute;left:589px;top:105px;width:376px;font-size:9.6px;line-height:1.35;text-align:justify}
.surv-text p{margin-bottom:12px}

/* final word */
.final{height:318px;background:linear-gradient(90deg,#13131c 0,#1a2034 60%,#0e1326)}
.final .img{left:690px;top:0;width:510px;height:318px;border-radius:0;background:radial-gradient(ellipse at 58% 52%,#e0623a 0,#8a2a22 18%,#1c2d52 45%,rgba(20,24,40,0) 75%)}
.final h2{position:absolute;left:246px;top:78px;font-size:15px;color:#fff}
.final .rule{position:absolute;left:246px;top:106px;margin:0}
.final p{position:absolute;left:246px;top:142px;width:350px;color:#d9dbe3;font-size:11px;line-height:1.7}

/* footer */
.site-footer{height:333px;background:var(--dark)}
.f-brand{position:absolute;left:250px;top:38px;display:flex;align-items:center;gap:6px;color:var(--blue);font-weight:800;font-size:11px}
.f-brand i{display:block;width:16px;height:16px;border:2px solid var(--blue);border-radius:50%}
.f-contact{position:absolute;left:250px;top:80px;color:#fff;font-size:10px;line-height:1.9}
.f-donate{position:absolute;left:250px;top:130px;width:83px;height:33px;border-radius:17px;background:var(--blue);color:#fff;font-size:8.5px;font-weight:700;display:flex;align-items:center;justify-content:center;gap:4px}
.f-col{position:absolute;top:48px;color:#d6d7de;font-size:9.5px}
.f-col h4{color:#fff;font-size:10px;font-weight:800;margin-bottom:20px}
.f-col li{margin-bottom:13px}
.f-col .faded{color:#5a5b66}
.f-col .signup{color:var(--orange)}
.socials{position:absolute;left:437px;top:174px;display:flex;gap:10px}
.socials span{width:20px;height:20px;border-radius:50%;border:1px solid #3b3c48}
.f-rule{position:absolute;left:250px;top:250px;width:715px;height:1px;background:#2c2d38}
.f-legal{position:absolute;left:250px;top:262px;color:#fff;font-size:9px;line-height:1.8}
</style>
</head>
<body>

<div class="topbar"><div class="date"><b>01</b>DEC<br>2022</div></div>

<header class="site-header">
  <div class="brand"><i></i>Velundaro Family</div>
  <nav class="nav">
    <span class="active">Home</span><span class="dd">Research</span><span>Impact</span><span>In Memory Of</span><span class="dd">Ways To Help</span><span class="dd">Events</span><span class="dd">Media</span><span class="dd">About</span>
  </nav>
  <div class="donate-top">DONATE <svg width="9" height="8" viewBox="0 0 10 9"><path d="M5 9 0.8 4.6A2.4 2.4 0 0 1 5 1.5a2.4 2.4 0 0 1 4.2 3.1Z" fill="#e0331c"/></svg></div>
</header>

<section class="hero">
  <h1>About Stomach Cancer: Types, Causes, Symptoms,&nbsp; Treatments, Cures and Research</h1>
  <div class="rule"></div>
  <p>Let's go through the different causes and symptoms of stomach cancer. Then, we'll touch on some of the current ways to diagnose and treat stomach cancer. Finally, we'll discuss the survival rates and research concerning stomach cancer.&nbsp; This guide is based on information from the National Oncology Bureau (NOB), the U.S. government's principal agency for cancer research.</p>
  <div class="img" role="img" aria-label="Doctor in gloves holding a glass panel showing the digestive organs"></div>
</section>

<section class="causes">
  <h2 class="sec-title">Possible Causes of Stomach Cancer</h2>
  <p class="sec-lead">Stomach cancer occurs for many reasons. For some people, genetics plays a significant role. Here are some of the biggest risk factors associated with stomach cancer.</p>
  <div class="rule center"></div>
  <div class="img" role="img" aria-label="X-ray style illustration of the torso with the stomach glowing red"></div>
  <div class="cond-box">
    <h3>Having any of the following medical conditions</h3>
    <ul class="dots">
      <li>Helicobacter pylori (H. pylori) infection of the stomach</li>
      <li>Chronic gastritis (inflammation of the stomach)</li>
      <li>Pernicious anemia</li>
      <li class="gap">Intestinal metaplasia (a condition in which the normal stomach lining is replaced with the cells that line the intestines)</li>
      <li>Gastric polyps</li>
      <li>Epstein-Barr virus infection</li>
      <li>Familial syndromes (including familial adenomatous polyposis)</li>
    </ul>
  </div>
  <ul class="tri risk-list">
    <li>Eating a diet high in salted, smoked foods and low in fruits and vegetables.</li>
    <li>Eating foods that have not been prepared or stored properly.</li>
    <li>Being older or male.</li>
    <li>Smoking cigarettes.</li>
    <li>Having a mother, father, sister, or brother who has had stomach cancer.</li>
  </ul>
</section>

<section class="symptoms">
  <h2 class="sec-title">Stomach Cancer Symptoms</h2>
  <div class="rule center"></div>
  <article class="card early">
    <div class="img" role="img" aria-label="Person holding their abdomen in discomfort"></div>
    <div class="card-body">
      <h3>In the early stages of stomach cancer, the following signs and symptoms may occur:</h3>
      <ul class="tri">
        <li>Indigestion and stomach discomfort</li>
        <li class="hl">A bloated feeling after eating</li>
        <li>Mild nausea</li>
        <li class="hl">Loss of appetite</li>
        <li>Heartburn</li>
      </ul>
    </div>
  </article>
  <article class="card late">
    <div class="img" role="img" aria-label="Woman holding her chest in pain at home"></div>
    <div class="card-body">
      <h3>In more advanced stages of stomach cancer, the following signs and symptoms may occur:</h3>
      <ul class="tri">
        <li>Blood in the stool</li>
        <li class="hl">Vomiting</li>
        <li>Weight loss for no known reason</li>
        <li class="hl">Stomach pain</li>
        <li>Jaundice (yellowing of eyes and skin)</li>
        <li class="hl">Ascites (build-up of fluid in the abdomen)</li>
        <li>Trouble swallowing</li>
      </ul>
    </div>
  </article>
</section>

<section class="diagnosis">
  <h2>Stomach Cancer Diagnosis</h2>
  <div class="rule"></div>
  <p class="intro">If you or your doctor suspect you may have stomach cancer, make an appointment with a gastroenterologist, which is a doctor who specializes in the digestive system. During an appointment, they will ask you to provide them with stool and blood samples alongside a thorough physical examination.</p>
  <div class="img a" role="img" aria-label="Doctor with stethoscope holding a glowing stomach model"></div>
  <div class="img b" role="img" aria-label="Illustration of a body with cancer cells around the intestines"></div>
  <div class="imaging">
    <h3>They may also ask for imaging, including an:</h3>
    <ul class="tri">
      <li>Upper gastrointestinal endoscopy where a doctor inserts a thin, lighted tube (an endoscope) into your mouth, down your esophagus, and into your stomach while you're sedated or under anesthesia. The endoscope allows your doctor to look at the inner lining of the stomach wall. It can also be used to take a sample (biopsy) of any areas your doctor wants analyzed by a pathologist (a doctor who specializes in diagnosing disease).</li>
      <li>Barium swallow X-rays or upper GI series. In this text you drink a liquid solution containing barium, a silver-white metal that shows up on an X-ray and helps doctors see a clear image of any potential abnormalities</li>
      <li>CT scan (CAT scan). A CT scan is a procedure that makes a series of detailed pictures of areas inside the body that are then linked to an X-ray machine.</li>
    </ul>
    <p class="after">Other tests will likely follow.</p>
  </div>
</section>

<section class="treatments">
  <h2>Stomach Cancer Cure and Treatments</h2>
  <div class="rule"></div>
  <div class="treat-text">
    <p>In most cases, stomach cancers are only cured when diagnosed in the early stages. Stomach cancer has a five-year survival rate of 33.3 percent.</p>
    <p>Doctors will use some or all of the following treatments in an attempt to get your stomach cancer into remission including surgery, endoscopic mucosal resection, chemotherapy, radiation therapy, chemoradiation, targeted therapy and immunotherapy.</p>
    <p>Surgery is a common treatment for stomach cancer. The most common surgeries used include subtotal gastrectomy and total gastrectomy. The following procedures can be preformed if the tumor is blocking the stomach but the cancer cannot be removed by standard surgery: endoluminal stent placement, endoluminal laser therapy and gastrojejunostomy.</p>
    <p>Endoscopic mucosal resection is a procedure that uses an endoscope to remove any precancerous groths or early stage cancer from digestive tract lining without surgery.</p>
    <p>Radiation therapy targets cancer cells by using high- energy X-rays or radiation beams to keep them from growing. This type of treatment can be customized to each patient depending on the type and stage of the cancer being treated.</p>
    <p>Chemotherapy involves very strong drugs that kill cancerous cells and can prevent them from coming back. Chemoradiation therapy combines chemotherapy and radiation therapy to increase the effects of both.</p>
    <p>Targeted therapy uses drugs or other substances to target and attack cancer cells. Usually, targeted therapies are less harmful than chemotherapy or radiation therapy. Patients have special nutritional needs during esophageal cancer treatments.</p>
    <p>Immunotherapy is a treatment that uses the patient's immune system to fight cancer</p>
  </div>
  <div class="img" role="img" aria-label="Seated patient holding her stomach during a medical consultation"></div>
</section>

<section class="survival">
  <div class="img" role="img" aria-label="Doctor's hand pointing at a sketched stomach illustration"></div>
  <h2>Stomach Cancer Survival Rates</h2>
  <div class="rule"></div>
  <div class="surv-text">
    <p>When people measure the survival rates of cancer, they primarily focus on the five-year survival rate. The five-year survival rate measures how many people with a certain type of cancer survived five years or more after diagnosis and the beginning of treatment.</p>
    <p>The Registry, Outcomes and Survival Tracking (ROST) program keeps track of cancer statistics in the United States. They also have a system to judge where cancer is in its growth cycle. There are three categories—localized, regional, and distant.</p>
    <p>Localized refers to cancer that only exists in the area where cancerous growth began. The initial cancerous growth has not spread to any other part of the body. The five-year survival rate for localized stomach cancer is 71.8%.</p>
    <p>Regional refers to cancer that has spread from its original location, but not to places far away. In the case of stomach cancer, this could mean spreading to the esophagus or colon among other locations. The five-year survival rate for regional stomach cancer is 32.9%.</p>
    <p>Distant refers to cancer that has spread to places far from the original location of the cancerous growth. This could mean spreading to the lungs, brain, blood or any other part of your body. The five-year survival rate for distant stomach cancer is 5.9%.</p>
  </div>
</section>

<section class="final">
  <div class="img" role="img" aria-label="Glowing red illustration of the stomach and intestines on a dark background"></div>
  <h2>Final Word</h2>
  <div class="rule"></div>
  <p>Stomach cancer represents almost 1.4 percent of all new cancer cases in the US. Many factors influence the risk of getting stomach cancer. If you believe you are at risk of stomach cancer or exhibit any of the associated symptoms, contact your healthcare provide right away.</p>
</section>

<footer class="site-footer">
  <div class="f-brand"><i></i>Velundaro Family</div>
  <div class="f-contact">(212) 555-0148<br>mara@velundaro.org</div>
  <div class="f-donate">DONATE <svg width="9" height="8" viewBox="0 0 10 9"><path d="M5 9 0.8 4.6A2.4 2.4 0 0 1 5 1.5a2.4 2.4 0 0 1 4.2 3.1Z" fill="#fff"/></svg></div>
  <div class="f-col" style="left:437px">
    <h4>ABOUT</h4>
    <ul><li style="margin-top:14px">Who We Are / Contact Us</li><li>Board Of Directors</li><li>Stomach and Esophageal Cancers</li></ul>
  </div>
  <div class="socials"><span></span><span></span><span></span><span></span></div>
  <div class="f-col" style="left:624px">
    <h4>WAYS TO HELP</h4>
    <ul><li>Donate</li><li>Run With Us!</li><li>Annual Gala</li><li>Funds – Research – Actions</li></ul>
  </div>
  <div class="f-col" style="left:811px">
    <h4>MEDIA</h4>
    <ul><li class="faded">Photos</li><li>Video</li><li>Press</li><li class="signup" style="margin-top:20px">Sign up for our Email Mailing List.</li></ul>
  </div>
  <div class="f-rule"></div>
  <div class="f-legal">The Velundaro Family Foundation is a designated 501(c)3<br>© 2020 Velundaro Family Foundation. All Rights Reserved. Help Us Turn Fact Into Fiction</div>
</footer>

</body>
</html>
```